Create Bourbon label for Craft Distillery located in the Foothills of NC.

Need to create a label for a craft bourbon. The brand name is Brookfen. Looking for a traditional/vintage bottle label. I have created a concept and would like an expansion of the concept idea (open to artwork outside of concept art as well). I have included the bottle being used. Label area approx 4.25H x 3.5W. With the Brookfen brand name, would like to incorporate trees (native to NC and Appalachia), mountains (mt pano of area included), and sawblade. However, I do not want the sawblade to be the focal point of the design. The word Bourbon, proof, abv, and 750 ml will need to be horizontal. Brookfen and Made in NC can be angled in the design.

Requirements
Must have
• Front Label will need to contain the followingBrand Name = SawmillsBourbon750 ml100 Proof50% ABVAged 3 years

```html
<!DOCTYPE html>
<html lang="en">
<head>
<meta charset="utf-8">
<title>Brookfen Bourbon Label</title>
<link rel="stylesheet" href="https://fonts.googleapis.com/css2?family=Abril+Fatface&display=swap">
<style>
  :root {
    --page: #ffffff;
    --frame-black: #000000;
    --frame-line: #f2f2f2;
    --wood-dark: #15110c;
    --wood-mid: #3a2f21;
    --gold-dark: #b8832e;
    --gold-light: #f2cd6e;
    --steel: #d1d3d4;
    --ink: #111111;
    --label-white: #f3f3f5;
    --shadow-grey: #55555a;
  }
  html, body {
    margin: 0;
    padding: 0;
    width: 1200px;
    height: 1200px;
    overflow: hidden;
    background: var(--page);
  }
  .label {
    display: block;
    width: 1200px;
    height: 1200px;
  }
  .label-outer { fill: var(--frame-black); }
  .label-rule { fill: none; stroke: var(--frame-line); stroke-width: 6; }
  .inner-plate { fill: var(--steel); }
  .name-band { fill: var(--frame-black); }
  .brand-name {
    font-family: "Abril Fatface", serif;
    font-size: 168px;
    fill: var(--gold-light);
  }
  .origin {
    font-family: "Abril Fatface", serif;
    font-size: 46px;
    fill: var(--ink);
  }
  .strength {
    font-family: "Abril Fatface", serif;
    font-size: 28px;
    fill: var(--ink);
  }
  .spirit-type {
    font-family: "Abril Fatface", serif;
    font-size: 112px;
    fill: var(--label-white);
  }
  .spirit-type-shadow { fill: var(--shadow-grey); }
  .volume {
    font-family: "Abril Fatface", serif;
    font-size: 40px;
    fill: var(--label-white);
    letter-spacing: 1px;
  }
</style>
</head>
<body>
<svg class="label" viewBox="0 0 1500 1500" xmlns="http://www.w3.org/2000/svg">
  <defs>
    <linearGradient id="gold-sheen" x1="0" y1="0" x2="1" y2="0">
      <stop offset="0" stop-color="var(--gold-dark)"/>
      <stop offset="0.55" stop-color="var(--gold-light)"/>
      <stop offset="1" stop-color="var(--gold-dark)"/>
    </linearGradient>
    <linearGradient id="wood-tone" x1="0" y1="0" x2="1" y2="0">
      <stop offset="0" stop-color="var(--wood-dark)"/>
      <stop offset="0.3" stop-color="var(--wood-mid)"/>
      <stop offset="0.5" stop-color="var(--wood-dark)"/>
      <stop offset="0.75" stop-color="var(--wood-mid)"/>
      <stop offset="1" stop-color="var(--wood-dark)"/>
    </linearGradient>
    <path id="label-shape" d="M292 295 Q370 270 390 195 L525 195 C640 195 640 97 760 97 C880 97 900 195 990 195 L1125 195 Q1145 270 1222 295 L1222 1275 Q1145 1300 1125 1375 L390 1375 Q370 1300 292 1275 Z"/>
  </defs>

  <use href="#label-shape" class="label-outer"/>
  <use href="#label-shape" class="label-rule" transform="translate(757 735) scale(0.953 0.966) translate(-757 -735)"/>
  <use href="#label-shape" class="label-field" fill="url(#wood-tone)" transform="translate(757 735) scale(0.931 0.95) translate(-757 -735)" role="img" aria-label="Dark vertical wood grain texture"/>

  <rect class="tree-line" x="545" y="250" width="465" height="270" rx="40" fill="url(#gold-sheen)" role="img" aria-label="Gold silhouette of a row of Appalachian evergreen trees"/>

  <circle class="saw-blade" cx="812" cy="805" r="318" fill="url(#gold-sheen)" role="img" aria-label="Gold circular sawblade with teeth around the rim"/>
  <circle class="inner-plate" cx="800" cy="785" r="245"/>

  <g class="brand-lockup" transform="rotate(-10 760 560)">
    <rect class="name-band" x="335" y="455" width="850" height="175" rx="18"/>
    <text class="brand-name" x="760" y="600" text-anchor="middle">Brookfen</text>
  </g>

  <text class="origin" x="800" y="775" text-anchor="middle" transform="rotate(-15 800 765)">Made in NC</text>

  <text class="strength" x="720" y="898" text-anchor="middle">100 proof</text>
  <text class="strength" x="882" y="898" text-anchor="middle">50% abv</text>

  <text class="spirit-type spirit-type-shadow" x="764" y="1190" text-anchor="middle">BOURBON</text>
  <text class="spirit-type" x="756" y="1186" text-anchor="middle">BOURBON</text>

  <text class="volume" x="757" y="1312" text-anchor="middle">750 ml</text>
</svg>
</body>
</html>
```